4 'Thank you' greetings cards designs

We are a small greetings card publisher and we need designs for a range of 'Thank you' greetings cards and notecards.
This project is for a total of 4 designs.
Please take a look at this board on Moodpinly, to see the kind of thing we are looking for: https://www.moodpinly.example/dorvek481/thank-you-cards/
The cards will be printed at a maximum size of 131mm x 183mm (including a 3mm bleed) so please provide 300dpi CMYK files at this size. Please ensure that any text (or elements of the design that are not part of the bleed) are at least 11mm in from each edge. Also, please note that cards do not have to have a bleed if your design doesn't require it (e.g. a plain white background).
Please provide 2 designs in 'portrait' orientation and 2 in 'landscape'.
Please provide 2 designs that just have the words 'Thank you' and then 2 designs that include your choice of these alternative messages:
Thank you so much
Thanks very much
Thank you very much
Thanks a million
Just to say thank you
A big thank you
A really big thank you
Feel free to use an exclamation mark on a couple of your designs, if you wish!
Other than the above guidelines, everything else is up to you in terms of colours, fonts, shapes, etc. - but please use the Moodpinly board to see the kind of designs we are looking for.
Thank you!

```html
<!DOCTYPE html>
<html lang="en">
<head>
<meta charset="utf-8">
<title>Thanks so much – greeting card</title>
<link rel="stylesheet" href="https://fonts.googleapis.com/css2?family=Herr+Von+Muellerhoff&display=swap">
<style>
  :root {
    --card-green: #0b3019;
    --frame-yellow: #e8cf00;
    --petal-yellow: #e6cc0a;
    --ink-white: #ffffff;
    --script: "Herr Von Muellerhoff", cursive;
  }
  html, body {
    margin: 0;
    padding: 0;
    width: 1200px;
    height: 1000px;
    overflow: hidden;
    background: var(--card-green);
  }
  .card {
    position: relative;
    width: 1200px;
    height: 1000px;
    background: var(--card-green);
    overflow: hidden;
  }
  .card__frame {
    position: absolute;
    left: 35px;
    top: 28px;
    width: 1142px;
    height: 944px;
    box-sizing: border-box;
    border: 4px solid var(--frame-yellow);
  }
  .flower-cluster {
    position: absolute;
    border-radius: 50%;
    background: radial-gradient(circle at 50% 50%,
      rgba(230, 204, 10, 0.55) 0%,
      rgba(230, 204, 10, 0.3) 45%,
      rgba(230, 204, 10, 0) 72%);
  }
  .flower-cluster--top-right {
    left: 800px;
    top: 50px;
    width: 360px;
    height: 360px;
  }
  .flower-cluster--bottom-left {
    left: 50px;
    top: 592px;
    width: 365px;
    height: 350px;
  }
  .greeting {
    margin: 0;
    font-family: var(--script);
    font-weight: 400;
    color: var(--ink-white);
  }
  .greeting__line {
    position: absolute;
    left: 0;
    width: 1200px;
    text-align: center;
    line-height: 1;
    white-space: nowrap;
  }
  .greeting__line--thanks {
    top: 170px;
    font-size: 300px;
    padding-left: 10px;
    box-sizing: border-box;
  }
  .greeting__line--so {
    top: 515px;
    font-size: 110px;
    padding-left: 10px;
    box-sizing: border-box;
  }
  .greeting__line--much {
    top: 660px;
    font-size: 190px;
    padding-left: 55px;
    box-sizing: border-box;
  }
</style>
</head>
<body>
  <main class="card">
    <div class="card__frame"></div>

    <div class="flower-cluster flower-cluster--top-right" role="img"
         aria-label="Cluster of three yellow outlined five-petal flowers with white centres"></div>
    <div class="flower-cluster flower-cluster--bottom-left" role="img"
         aria-label="Cluster of three yellow outlined five-petal flowers with white centres"></div>

    <h1 class="greeting">
      <span class="greeting__line greeting__line--thanks">Thanks</span>
      <span class="greeting__line greeting__line--so">so</span>
      <span class="greeting__line greeting__line--much">much</span>
    </h1>
  </main>
</body>
</html>
```